New business card for UK roofing company

We are Brindmore Roofing and we need a business card design for our staff.

We offer the following services:

- New roofs
- General roof repairs
- Drone surveys
- Single ply roofing
- Steel cladding
- Asbestos removal
- Electronic leak detection

I have attached our logo. I have also attached example branding printed to our vans. The business card should fit in with the style of our branding.

The business card should have the following information;

Address:
Unit 17c Wendlecroft Farm
Wendlecroft Lane
Hatchington
CM4 9QD

Telephone: 020 7946 0372
24 Hour: 0800 612 4479

Email: ray@brindmoreroofing.example
Mobile: 07700981234
Name: Ray Tunstead
Website: www.brindmoreroofing.example

The business card will be printed in Spot UV, see here: https://www.kestaprint.example/business-cards/spot-uv/

If you need anymore info, please let me know,

```html
<!DOCTYPE html>
<html lang="en">
<head>
<meta charset="utf-8">
<title>Brindmore Roofing – Business Card</title>
<link rel="stylesheet" href="https://fonts.googleapis.com/css2?family=Montserrat:wght@300;400;700;800&display=swap">
<style>
  :root {
    --navy: #0b3f7a;
    --navy-deep: #003b74;
    --cyan: #0abde6;
    --cyan-soft: #4fc7ea;
    --pale: #e3f5fb;
    --white: #ffffff;
    --backdrop: #dcdcdc;
  }
  * { box-sizing: border-box; margin: 0; padding: 0; }
  html, body {
    width: 1200px; height: 846px; overflow: hidden;
    background: var(--backdrop);
    font-family: "Montserrat", sans-serif;
  }
  .card {
    position: absolute; top: 255px;
    width: 520px; height: 336px;
    background: var(--white);
    overflow: hidden;
    box-shadow: 0 10px 24px rgba(0,0,0,.18);
  }
  .card--front { left: 50px; }
  .card--back { left: 630px; }

  /* wordmark */
  .wordmark { display: flex; align-items: center; gap: 8px; }
  .wordmark__dot { width: 22px; height: 22px; border-radius: 50%; background: var(--navy); }
  .wordmark__name { font-weight: 800; font-size: 22px; color: var(--navy); letter-spacing: -0.5px; }

  /* front */
  .card--front .wordmark { position: absolute; left: 34px; top: 36px; }
  .person { position: absolute; left: 34px; top: 118px; font-weight: 800; font-size: 19px; }
  .person__first { color: var(--navy); }
  .person__last { color: var(--cyan); }
  .contacts { position: absolute; left: 34px; top: 160px; right: 24px; display: flex; gap: 22px; }
  .contacts__col { font-size: 11.5px; line-height: 1.55; color: var(--navy); font-weight: 300; }
  .contacts__label { color: var(--cyan); font-weight: 700; }
  .divider { position: absolute; left: 34px; right: 34px; top: 240px; height: 1px; background: var(--cyan-soft); }
  .address { position: absolute; left: 34px; top: 254px; font-size: 11.5px; font-weight: 300; color: var(--navy); }

  /* back */
  .back-art { position: absolute; inset: 0; }
  .service-block { position: absolute; left: 26px; top: 34px; color: var(--white); }
  .hotline { display: flex; align-items: center; gap: 10px; }
  .hotline__badge { width: 46px; height: 46px; }
  .hotline__number { font-weight: 800; font-size: 25px; letter-spacing: .3px; }
  .services { list-style: none; margin-top: 18px; font-weight: 800; font-size: 11.5px; line-height: 1.75; text-transform: uppercase; letter-spacing: .2px; }
  .services li::before { content: "• "; }
  .card--back .wordmark { position: absolute; right: 30px; bottom: 28px; }
</style>
</head>
<body>

<section class="card card--front" aria-label="Business card front">
  <div class="wordmark">
    <span class="wordmark__dot"></span>
    <span class="wordmark__name">brindmoreroofing</span>
  </div>
  <p class="person"><span class="person__first">Ray</span> <span class="person__last">Tunstead</span></p>
  <div class="contacts">
    <div class="contacts__col">
      <p><span class="contacts__label">Mobile:</span> 077 0098 1234</p>
      <p><span class="contacts__label">Telephone:</span> 020 7946 0372</p>
      <p><span class="contacts__label">24 Hour:</span> 0800 612 4479</p>
    </div>
    <div class="contacts__col">
      <p><span class="contacts__label">Email:</span> ray@brindmoreroofing.example</p>
      <p><span class="contacts__label">Website:</span> www.brindmoreroofing.example</p>
    </div>
  </div>
  <div class="divider"></div>
  <p class="address">Unit 17c Wendlecroft Farm, Wendlecroft Lane, Hatchington CM4 9QD</p>
</section>

<section class="card card--back" aria-label="Business card back">
  <svg class="back-art" viewBox="0 0 520 336" preserveAspectRatio="none" aria-hidden="true">
    <circle cx="420" cy="105" r="150" fill="var(--pale)"/>
    <polygon points="0,0 318,0 186,336 0,336" fill="var(--cyan-soft)"/>
    <polygon points="0,0 306,0 174,336 0,336" fill="var(--navy-deep)"/>
  </svg>
  <div class="service-block">
    <div class="hotline">
      <svg class="hotline__badge" viewBox="0 0 46 46" aria-hidden="true">
        <path d="M23 4 A19 19 0 1 1 6 15" fill="none" stroke="#fff" stroke-width="2.5" stroke-dasharray="4 3"/>
        <path d="M3 9 L6 16 L12 12" fill="none" stroke="#fff" stroke-width="2.5"/>
        <text x="23" y="23" text-anchor="middle" font-family="Montserrat, sans-serif" font-weight="800" font-size="11" fill="#fff">24/7</text>
        <text x="23" y="32" text-anchor="middle" font-family="Montserrat, sans-serif" font-weight="700" font-size="5.5" fill="#fff">SERVICE</text>
      </svg>
      <span class="hotline__number">0800 612 4479</span>
    </div>
    <ul class="services">
      <li>General roof repairs</li>
      <li>Drone roof surveys</li>
      <li>Single ply roofing</li>
      <li>Asbestos removal</li>
      <li>Steel cladding</li>
      <li>New roofs</li>
    </ul>
  </div>
  <div class="wordmark">
    <span class="wordmark__dot"></span>
    <span class="wordmark__name">brindmoreroofing</span>
  </div>
</section>

</body>
</html>
```